Plakate für Psychologische Beratung am Telefon
Zielgruppe
Psychologische Beratung am Telefon
Aufgabenstellung
anliegendes Word Dokument soll als eine Art 'Plakat' (pdf Datei) erstellt werden. Diese PDF Datei wird dann an alle MitarbeiterInnen gesandt und soll Auskunft über das Beratungsangebot geben. Die Farben bitte so wie auf dieser Website (das ist unser Mutterunternehmen). www.lindenhof-kolleg.com.

```html
<!DOCTYPE html>
<html lang="de">
<head>
<meta charset="utf-8">
<title>Beratungstelefon – Plakat</title>
<link rel="stylesheet" href="https://fonts.googleapis.com/css2?family=Open+Sans:wght@400;600;700&display=swap">
<style>
  :root {
    --brand-blue: #42669e;
    --ink: #1f1f1f;
    --paper: #ffffff;
    --sky-light: #dde7f6;
    --sky-mid: #c9d8f0;
    --panel-shadow: rgba(40, 60, 100, 0.25);
  }
  * { margin: 0; padding: 0; box-sizing: border-box; }
  html, body { width: 811px; height: 1200px; overflow: hidden; background: var(--paper); }
  body { font-family: "Open Sans", Arial, sans-serif; color: var(--ink); }

  .poster {
    position: relative;
    width: 811px; height: 1200px;
    background:
      radial-gradient(ellipse at 55% 70%, var(--paper) 0%, rgba(255,255,255,0) 60%),
      linear-gradient(135deg, var(--sky-light) 0%, #f2f6fc 45%, #eef3fb 70%, var(--sky-mid) 100%);
    overflow: hidden;
  }

  .brand {
    position: absolute; left: 470px; top: 70px;
    display: flex; align-items: center; gap: 10px;
    font-weight: 600; font-size: 19px; letter-spacing: 2px; color: var(--ink);
  }
  .brand-dot { width: 14px; height: 14px; border-radius: 50%; background: var(--brand-blue); }

  .headline { position: absolute; left: 40px; top: 126px; font-size: 30px; line-height: 43px; text-transform: uppercase; color: var(--ink); }
  .headline .light { font-weight: 400; }
  .headline .bold { font-weight: 700; }

  .white-band { position: absolute; left: 234px; top: 316px; width: 577px; height: 402px; background: var(--paper); }
  .rule { position: absolute; left: 0; top: 330px; width: 811px; height: 9px; background: var(--brand-blue); }

  .hotline-box {
    position: absolute; left: 0; top: 334px; width: 393px; height: 216px;
    background: var(--brand-blue); color: var(--paper);
    padding: 22px 0 0 29px; box-shadow: 3px 3px 6px var(--panel-shadow);
  }
  .hotline-box .intro { font-weight: 700; font-size: 16.5px; line-height: 29px; }
  .hotline-box .tel { font-weight: 700; font-size: 27px; line-height: 38px; }
  .hotline-box .offer { font-weight: 600; font-size: 16.5px; line-height: 29px; }
  .hotline-box .hours { font-weight: 400; font-size: 16px; line-height: 29px; }

  .photo {
    position: absolute; left: 393px; top: 339px; width: 418px; height: 379px;
    background: radial-gradient(ellipse at 60% 45%, #e9d6cc 0%, #d9c2bb 25%, #f3eeee 55%, #ffffff 80%);
  }

  .spine { position: absolute; left: 71px; top: 550px; width: 9px; height: 610px; background: var(--brand-blue); }

  .content-panel {
    position: absolute; left: 80px; top: 644px; width: 703px; height: 405px;
    background: linear-gradient(180deg, rgba(255,255,255,0.9), rgba(238,243,251,0.95));
    box-shadow: 2px 3px 6px var(--panel-shadow);
  }

  .tab {
    position: absolute; left: 80px; background: var(--brand-blue); color: var(--paper);
    font-weight: 700; font-size: 33px; line-height: 1; padding-left: 14px;
    display: flex; align-items: center; box-shadow: 3px 3px 5px var(--panel-shadow);
    text-transform: uppercase;
  }
  .tab-audience { top: 590px; width: 205px; height: 54px; }
  .tab-fields { top: 686px; width: 406px; height: 54px; }
  .tab-process { top: 887px; width: 233px; height: 48px; }

  .audience-text { position: absolute; left: 96px; top: 650px; font-size: 15px; }

  .field { position: absolute; top: 750px; font-size: 15px; line-height: 21.3px; }
  .field h3 { font-size: 15px; font-weight: 700; }
  .field-private { left: 95px; width: 215px; }
  .field-mental { left: 314px; width: 200px; }
  .field-work { left: 517px; width: 260px; }

  .process { position: absolute; left: 100px; top: 945px; font-size: 15px; }
  .process h3 { font-size: 17px; font-weight: 700; line-height: 24px; }
  .process ul { list-style: none; }
  .process li { line-height: 21.5px; padding-left: 24px; position: relative; }
  .process li::before { content: "•"; position: absolute; left: 2px; }

  .anonymity { position: absolute; left: 98px; top: 1077px; font-size: 15px; line-height: 20px; font-weight: 600; }
</style>
</head>
<body>
<main class="poster">
  <div class="brand"><span class="brand-dot"></span>LINDENHOF KOLLEG</div>

  <h1 class="headline">
    <span class="light">Das anonyme</span><br>
    <span class="bold">Beratungs- und Begleitangebot</span><br>
    <span class="bold">für MitarbeiterInnen &amp; Führungskräfte</span><br>
    <span class="light">in&nbsp; schwierigen Berufs- und Lebensphasen.</span>
  </h1>

  <div class="white-band"></div>
  <div class="rule"></div>

  <div class="photo" role="img" aria-label="Foto einer lächelnden Beraterin mit Headset"></div>

  <section class="hotline-box">
    <p class="intro">Das LHK Beratungs-Telefon des LHK<br>Lindenhof Kolleg für Weiterbildung.</p>
    <p class="tel">Tel.: 0451 – 552 70 – 410</p>
    <p class="offer">Sofortberatung oder Terminvereinbarung<br>zu Ihrer Wunschzeit</p>
    <p class="hours">Di. 14:00 – 17:00 Uhr &amp; Do. 9:00 – 12:00 Uhr</p>
  </section>

  <div class="spine"></div>
  <div class="content-panel"></div>

  <h2 class="tab tab-audience">Für wen?</h2>
  <p class="audience-text">Für alle Mitarbeitenden und Führungskräfte des LHK.</p>

  <h2 class="tab tab-fields">Die Beratungsfelder</h2>
  <div class="field field-private">
    <h3>Private Anliegen:</h3>
    <p>Partnerschaftskonflikte, Erziehungsberatung, Trennung/Scheidung, Verlust, Trauer, Todesfall, Schockdiagnosen usw.</p>
  </div>
  <div class="field field-mental">
    <h3>Psychische Gesundheit:</h3>
    <p>Sucht und Abhängigkeiten, Depressionen, Burnout, Ängste usw.</p>
  </div>
  <div class="field field-work">
    <h3>Berufliche Anliegen:</h3>
    <p>Vereinbarkeit Beruf und Familie, Konflikte mit Kolleginnen oder Kollegen oder Vorgesetzten, Überforderungen am Arbeitsplatz sowie Coaching für Führungskräfte</p>
  </div>

  <h2 class="tab tab-process">Der Ablauf</h2>
  <div class="process">
    <h3>Sie wählen 0451 552 70 410</h3>
    <ul>
      <li>Ihr Anruf wird von den psychologischen Assistentinnen angenommen</li>
      <li>Diese erfragen ein Stichwort zu Ihrem Anliegen, um Sie</li>
      <li>direkt mit einer Expertin oder einem Experten für Ihr Thema verbinden zu können</li>
    </ul>
  </div>

  <div class="anonymity">
    <p>Anonymität</p>
    <p>Die Beratung ist anonym. Sie müssen Ihren Namen nicht nennen.</p>
    <p>Unsere Beraterinnen und Berater verfügen alle über langjährige Beratungserfahrung</p>
    <p>und je nach Thema auch über eine Psychotherapiezulassung.</p>
  </div>
</main>
</body>
</html>
```